TV Antenna Installation business needs a unique flyer

We need a simple but effective flyer design for our TV Aerial installation company based in Newcastle, NSW, Australia called Bright Wave TV & Aerial Svcs.
We are trying to target areas where there has been a new transmitter installed and most houses just require their aerial redirecting and tv's retuning.

Industry/Entity Type

Business

Requirements
Must have
• We would like the idea of a headline phrase such as " Poor TV reception……..now a thing from the past" or something similar & catchy.
Also "Did you know a new transmitter has been recently installed in your area, we can therefore now GUARANTEE 100% PERFECT PICTURE
Charges from only $95.
- Free 5 year warranty
- Free signal testing
- Free Onsite Quote
Phone 0412 736 205
Nice to have
• Other services include:

- New Installs
- Extra Points & repairs
- TV wall mounting/Home Cinema
- Pull down tall masts

Modern tv picture, see example uploaded

```html
<!DOCTYPE html>
<html lang="en">
<head>
<meta charset="utf-8">
<title>Bright Wave TV &amp; Aerial Svcs – Flyer</title>
<link rel="stylesheet" href="https://fonts.googleapis.com/css2?family=Fredoka:wght@600&family=Comic+Neue:wght@700&family=Arimo:wght@400;700&family=Archivo+Black&family=Roboto+Condensed:wght@700&display=swap">
<style>
  :root {
    --navy: #2e3192;
    --red: #d0202e;
    --ink: #1f1f1f;
    --lime: #c6d82f;
    --sky-light: #f4f8fb;
    --sky-mid: #d6e4ef;
    --swoosh: #a9c6de;
  }
  * { margin: 0; padding: 0; box-sizing: border-box; }
  html, body { width: 884px; height: 1200px; overflow: hidden; background: #ffffff; }
  .flyer {
    position: relative; width: 884px; height: 1200px; overflow: hidden;
    background: radial-gradient(ellipse at 65% 45%, #ffffff 0%, var(--sky-light) 45%, var(--sky-mid) 100%);
  }
  .background-swirl {
    position: absolute; left: 0; top: 0; width: 480px; height: 1200px;
    background: linear-gradient(100deg, var(--swoosh) 0%, rgba(169, 198, 222, 0.55) 35%, rgba(255, 255, 255, 0) 80%);
  }
  .tv-illustration {
    position: absolute; left: 82px; top: 23px; width: 244px; height: 333px;
    background: linear-gradient(160deg, #d4e84a 0%, #a9c21c 70%, #6a7a1a 100%);
    border-radius: 40px 40px 20px 20px;
  }
  .brand-name {
    position: absolute; left: 380px; top: 66px; width: 436px; text-align: right;
    font-family: "Fredoka", sans-serif; font-weight: 600; font-size: 40px; line-height: 1.05;
    color: var(--navy);
  }
  .headline {
    position: absolute; left: 351px; top: 190px;
    font-family: "Comic Neue", cursive; font-weight: 700; font-size: 37px; line-height: 50px;
    color: var(--red);
  }
  .intro {
    position: absolute; left: 176px; top: 382px; width: 700px; text-align: center;
    font-family: "Arimo", sans-serif; font-weight: 700; font-size: 29px; line-height: 38.5px; color: var(--ink);
  }
  .intro strong { font-weight: 700; text-transform: uppercase; }
  .price {
    position: absolute; left: 247px; top: 554px; width: 600px; text-align: center;
    font-family: "Archivo Black", sans-serif; font-size: 43px; line-height: 54px; color: var(--red);
  }
  .benefits {
    position: absolute; left: 360px; top: 619px; width: 480px; list-style: none; text-align: center;
    font-family: "Archivo Black", sans-serif; font-size: 32px; line-height: 58px; color: var(--navy);
  }
  .services { position: absolute; left: 282px; top: 810px; width: 560px; height: 275px; }
  .services-shape { position: absolute; inset: 0; }
  .services-title {
    position: absolute; left: 96px; top: 40px;
    font-family: "Arimo", sans-serif; font-weight: 700; font-size: 37px; color: var(--red);
  }
  .services-list {
    position: absolute; left: 81px; top: 98px; list-style: none;
    font-family: "Arimo", sans-serif; font-weight: 700; font-size: 25px; line-height: 36.5px; color: var(--navy);
  }
  .services-list li { display: flex; align-items: center; gap: 14px; }
  .services-list svg { width: 24px; height: 22px; flex: none; }
  .phone {
    position: absolute; left: 436px; top: 1104px; display: flex; align-items: center; gap: 8px;
    font-family: "Roboto Condensed", sans-serif; font-weight: 700; font-size: 63px; color: var(--red);
  }
  .phone svg { width: 44px; height: 44px; }
</style>
</head>
<body>
<main class="flyer">
  <div class="background-swirl" role="img" aria-label="Decorative flowing light blue swoosh curves along the left side"></div>

  <div class="tv-illustration" role="img" aria-label="Illustration of a lime green retro television with antenna and a crossed-out screen"></div>

  <h1 class="brand-name">Bright Wave TV &amp;<br>Aerial Svcs</h1>

  <p class="headline">Poor TV reception……..<br>now a thing from the past</p>

  <p class="intro">Did you know a new transmitter<br>has been recently installed<br>in your area, we can therefore now<br><strong>Guarantee 100% perfect picture</strong></p>

  <p class="price">Charges from only $95</p>

  <ul class="benefits">
    <li>Free 5 year warranty</li>
    <li>Free signal testing</li>
    <li>Free Onsite Quote</li>
  </ul>

  <section class="services">
    <svg class="services-shape" viewBox="0 0 560 275" aria-hidden="true">
      <path d="M40 30 C60 10 90 6 140 8 C260 14 400 12 500 22 C530 26 545 50 552 100 C558 150 552 200 535 238 C520 265 490 269 440 269 C320 267 200 271 110 265 C60 261 35 248 22 213 C8 173 6 110 14 70 C20 50 28 40 40 30 Z" fill="var(--lime)" stroke="var(--red)" stroke-width="5"/>
    </svg>
    <h2 class="services-title">Our services</h2>
    <ul class="services-list">
      <li><svg viewBox="0 0 24 22" aria-hidden="true"><rect x="1" y="5" width="16" height="16" fill="#fff" stroke="var(--navy)" stroke-width="2"/><path d="M4 12 L9 17 L22 2" fill="none" stroke="var(--red)" stroke-width="3"/></svg>New Installs</li>
      <li><svg viewBox="0 0 24 22" aria-hidden="true"><rect x="1" y="5" width="16" height="16" fill="#fff" stroke="var(--navy)" stroke-width="2"/><path d="M4 12 L9 17 L22 2" fill="none" stroke="var(--red)" stroke-width="3"/></svg>Extra Points &amp; repairs</li>
      <li><svg viewBox="0 0 24 22" aria-hidden="true"><rect x="1" y="5" width="16" height="16" fill="#fff" stroke="var(--navy)" stroke-width="2"/><path d="M4 12 L9 17 L22 2" fill="none" stroke="var(--red)" stroke-width="3"/></svg>TV wall mounting/Home Cinema</li>
      <li><svg viewBox="0 0 24 22" aria-hidden="true"><rect x="1" y="5" width="16" height="16" fill="#fff" stroke="var(--navy)" stroke-width="2"/><path d="M4 12 L9 17 L22 2" fill="none" stroke="var(--red)" stroke-width="3"/></svg>Pull down tall masts</li>
    </ul>
  </section>

  <p class="phone">
    <svg viewBox="0 0 44 44" aria-hidden="true"><circle cx="22" cy="22" r="19" fill="none" stroke="var(--navy)" stroke-width="3"/><path d="M15 12 C12 14 12 20 16 26 C20 32 26 35 30 33 L31 29 L26 26 L24 28 C21 26 19 23 18 20 L20 18 L18 12 Z" fill="var(--navy)"/></svg>
    <span>0412 736 205</span>
  </p>
</main>
</body>
</html>
```